Copper Lantern Gin

The gin is 100% proof and men and anbody 18 - 30 year old will be a target market - the bottle is very distinctive and lends itself to a square label.

The bottle is curved with a large front face that lends itself to a striking design. There should be enough space around the label to show the black gin in the bottle as this is a feature.

The current bottle with the existing label is attached below as is the new glass bottle. The new gin will be coloured black.

Font styles to use
Decorative
Script

```html
<!DOCTYPE html>
<html lang="en">
<head>
<meta charset="utf-8">
<title>Copper Lantern Gin – Label</title>
<link href="https://fonts.googleapis.com/css2?family=Cinzel:wght@600;700&family=Pinyon+Script&family=Playfair+Display:wght@400&display=swap" rel="stylesheet">
<style>
  :root {
    --label-black: #0b0b0a;
    --label-edge: #141413;
    --gold-bright: #e8dfa6;
    --gold-mid: #a8974f;
    --gold-deep: #5d5223;
    --gold-line: #8f8136;
    --script-olive: #6d6537;
    --small-text: #7f7540;
  }
  * { margin: 0; padding: 0; box-sizing: border-box; }
  html, body {
    width: 1107px;
    height: 1200px;
    overflow: hidden;
    background: var(--label-edge);
  }
  .label {
    position: relative;
    width: 1107px;
    height: 1200px;
    background: radial-gradient(ellipse at 50% 40%, #121211 0%, var(--label-black) 70%);
  }
  .frame-outer {
    position: absolute;
    left: 35px; top: 33px;
    width: 1056px; height: 1131px;
    border: 2px solid var(--gold-line);
  }
  .frame-inner {
    position: absolute;
    left: 42px; top: 40px;
    width: 1042px; height: 1117px;
    border: 1px solid var(--gold-deep);
  }
  .backdrop-art {
    position: absolute;
    left: 120px; top: 60px;
    width: 880px; height: 1060px;
    background: radial-gradient(ellipse at 50% 45%, rgba(40,38,30,0.45) 0%, rgba(11,11,10,0) 65%);
  }
  .emblem {
    position: absolute;
    left: 376px; top: 98px;
    width: 353px; height: 268px;
    border-radius: 45%;
    background: radial-gradient(ellipse at 50% 50%, #7a6c3c 0%, #4d4321 55%, rgba(40,34,16,0.2) 100%);
  }
  .proof {
    position: absolute;
    right: 58px; top: 58px;
    font-family: "Pinyon Script", cursive;
    font-size: 44px;
    color: var(--gold-deep);
  }
  .brand-name {
    position: absolute;
    left: 0; width: 1107px; top: 420px;
    text-align: center;
    font-family: "Cinzel", serif;
    font-weight: 700;
    font-size: 62px;
    letter-spacing: 2px;
    line-height: 1;
    background: linear-gradient(180deg, var(--gold-bright) 0%, var(--gold-mid) 55%, var(--gold-deep) 100%);
    -webkit-background-clip: text;
    background-clip: text;
    color: transparent;
  }
  .product {
    position: absolute;
    left: 0; width: 1107px; top: 508px;
    text-align: center;
    font-family: "Cinzel", serif;
    font-weight: 700;
    font-size: 126px;
    letter-spacing: 4px;
    line-height: 1;
    background: linear-gradient(180deg, var(--gold-bright) 0%, var(--gold-mid) 55%, var(--gold-deep) 100%);
    -webkit-background-clip: text;
    background-clip: text;
    color: transparent;
  }
  .rule {
    position: absolute;
    width: 255px; height: 21px;
    border-top: 3px solid var(--gold-mid);
    border-bottom: 3px solid var(--gold-mid);
    top: 549px;
  }
  .rule-left { left: 133px; }
  .rule-right { left: 729px; }
  .tagline {
    position: absolute;
    left: 0; width: 1107px; top: 720px;
    text-align: center;
    font-family: "Pinyon Script", cursive;
    font-size: 42px;
    color: var(--script-olive);
  }
  .abv, .volume {
    position: absolute;
    top: 1112px;
    font-family: "Playfair Display", serif;
    font-size: 25px;
    color: var(--small-text);
  }
  .abv { left: 62px; }
  .volume { right: 58px; }
</style>
</head>
<body>
  <main class="label">
    <div class="backdrop-art" role="img" aria-label="Faint dark illustration of a hound in the label background"></div>
    <div class="frame-outer"></div>
    <div class="frame-inner"></div>
    <div class="emblem" role="img" aria-label="Gold ornamental crest framing an illustration of a hound"></div>
    <p class="proof">100% Proof</p>
    <h1 class="brand-name">Copper Lantern</h1>
    <span class="rule rule-left"></span>
    <p class="product">GIN</p>
    <span class="rule rule-right"></span>
    <p class="tagline">Navy Strength British Gin</p>
    <p class="abv">57%abv</p>
    <p class="volume">750ML</p>
  </main>
</body>
</html>
```